Bright Fern Property Services

Design a billboard with our logo that includes bullet points for
Property Maintenance, Plumbing, and Electrical, licensed and insured.
Phone number 865 471 3908

also add the website brightfernps-example.com

```html
<!DOCTYPE html>
<html lang="en">
<head>
<meta charset="utf-8">
<title>Bright Fern Property Services – Billboard</title>
<link rel="stylesheet" href="https://fonts.googleapis.com/css2?family=Montserrat:wght@600;700&family=Oswald:wght@500;600&display=swap">
<style>
  :root {
    --green: #4ba524;
    --green-dark: #3f8f1c;
    --ink: #1d1d1d;
    --panel: #f3f4f0;
    --page: #e4e8ec;
    --white: #ffffff;
    --photo-sky: #d9dde0;
    --photo-wall: #7b7d78;
    --photo-roof: #8a6a58;
  }
  * { margin: 0; padding: 0; box-sizing: border-box; }
  html, body {
    width: 1200px;
    height: 1095px;
    overflow: hidden;
    background: var(--page);
  }
  .billboard {
    position: absolute;
    left: 20px;
    top: 295px;
    width: 1160px;
    height: 505px;
    background: var(--panel);
    overflow: hidden;
    box-shadow: 0 2px 6px rgba(0,0,0,0.12);
  }
  .brand {
    position: absolute;
    left: 190px;
    top: 56px;
    width: 350px;
    color: var(--green);
    font-family: "Montserrat", sans-serif;
    font-weight: 700;
    text-align: center;
    white-space: nowrap;
  }
  .brand-name {
    font-size: 40px;
    line-height: 1;
    letter-spacing: 1px;
  }
  .brand-sub {
    margin-top: 10px;
    font-size: 17px;
    letter-spacing: 3px;
    line-height: 1.1;
  }
  .brand-rule {
    margin: 8px auto 0;
    width: 270px;
    height: 2px;
    background: var(--green);
  }
  .services {
    position: absolute;
    left: 60px;
    top: 190px;
    display: flex;
    list-style: none;
  }
  .service {
    display: flex;
    flex-direction: column;
    align-items: center;
  }
  .service-icon { width: 82px; height: 88px; }
  .service-label {
    margin-top: 20px;
    font-family: "Oswald", sans-serif;
    font-weight: 500;
    font-size: 27px;
    color: var(--ink);
    white-space: nowrap;
  }
  .service--maintenance { width: 250px; }
  .service--plumbing { width: 190px; }
  .service--electrical { width: 170px; }
  .credentials {
    position: absolute;
    left: 230px;
    top: 368px;
    width: 310px;
    text-align: center;
    font-family: "Oswald", sans-serif;
    font-weight: 600;
    font-style: italic;
    font-size: 27px;
    letter-spacing: 1.5px;
    color: var(--green);
  }
  .phone-pill {
    position: absolute;
    left: 0;
    top: 420px;
    width: 459px;
    height: 60px;
    background: var(--green);
    border-radius: 0 30px 30px 0;
    display: flex;
    align-items: center;
    padding-left: 42px;
    gap: 16px;
  }
  .phone-icon { width: 44px; height: 44px; }
  .phone-number {
    font-family: "Montserrat", sans-serif;
    font-weight: 700;
    font-size: 38px;
    color: var(--white);
    letter-spacing: 1px;
  }
  .website {
    position: absolute;
    left: 474px;
    top: 436px;
    font-family: "Oswald", sans-serif;
    font-weight: 500;
    font-size: 18px;
    letter-spacing: 0.5px;
    color: var(--ink);
    white-space: nowrap;
  }
  .feature-frame {
    position: absolute;
    left: 0;
    top: 0;
    width: 1160px;
    height: 505px;
  }
</style>
</head>
<body>
  <main class="billboard">
    <svg class="feature-frame" viewBox="0 0 1160 505" aria-hidden="true">
      <path d="M800 0 H1160 V505 H792 L682 282 Q666 247 682 212 Z" fill="var(--green)"/>
    </svg>
    <svg class="feature-frame" viewBox="0 0 1160 505" role="img" aria-label="Photograph of a large two-storey suburban house with grey siding, brown roof and stone porch">
      <defs>
        <linearGradient id="house-photo" x1="0" y1="0" x2="0" y2="1">
          <stop offset="0" stop-color="var(--photo-sky)"/>
          <stop offset="0.35" stop-color="var(--photo-roof)"/>
          <stop offset="0.7" stop-color="var(--photo-wall)"/>
          <stop offset="1" stop-color="#6f6a5e"/>
        </linearGradient>
      </defs>
      <path d="M836 0 H1160 V505 H826 L720 282 Q705 247 720 212 Z" fill="url(#house-photo)"/>
    </svg>

    <header class="brand">
      <div class="brand-name">BRIGHT FERN</div>
      <div class="brand-sub">PROPERTY SERVICES LLC</div>
      <div class="brand-rule"></div>
    </header>

    <ul class="services">
      <li class="service service--maintenance">
        <svg class="service-icon" viewBox="0 0 82 88" fill="none" stroke="var(--green)" stroke-width="3" stroke-linejoin="round" stroke-linecap="round" aria-hidden="true">
          <path d="M28 30 L45 16 L62 30 V52 H28 Z"/>
          <circle cx="45" cy="38" r="7"/>
          <circle cx="45" cy="38" r="2.5"/>
          <path d="M4 70 L16 60 Q24 56 32 60 L46 62 Q52 64 48 68 L34 68"/>
          <path d="M48 66 L68 56 Q76 54 74 62 L52 80 H26 L14 86"/>
        </svg>
        <span class="service-label">PROPERTY MAINTENANCE</span>
      </li>
      <li class="service service--plumbing">
        <svg class="service-icon" viewBox="0 0 82 88" fill="none" stroke="var(--green)" stroke-width="3" stroke-linejoin="round" stroke-linecap="round" aria-hidden="true">
          <rect x="4" y="12" width="74" height="18" rx="2"/>
          <line x1="18" y1="8" x2="18" y2="34"/>
          <line x1="34" y1="8" x2="34" y2="34"/>
          <line x1="58" y1="8" x2="58" y2="34"/>
          <path d="M14 40 Q10 46 14 48 Q18 46 14 40 Z" fill="var(--green)"/>
          <path d="M34 40 Q28 48 34 56 L64 84 H76 L44 50 Q48 42 42 38"/>
        </svg>
        <span class="service-label">PLUMBING</span>
      </li>
      <li class="service service--electrical">
        <svg class="service-icon" viewBox="0 0 82 88" fill="none" stroke="var(--green)" stroke-width="3" stroke-linejoin="round" stroke-linecap="round" aria-hidden="true">
          <circle cx="41" cy="44" r="30" stroke-dasharray="10 6"/>
          <circle cx="41" cy="44" r="24"/>
          <path d="M45 28 L33 47 H42 L37 61 L50 41 H41 Z"/>
        </svg>
        <span class="service-label">ELECTRICAL</span>
      </li>
    </ul>

    <p class="credentials">LICENSED AND INSURED</p>

    <div class="phone-pill">
      <svg class="phone-icon" viewBox="0 0 44 44" aria-hidden="true">
        <circle cx="22" cy="22" r="22" fill="var(--white)"/>
        <path d="M15 11 L19 11 L21 18 L18 20 Q20 25 24 27 L26 24 L33 26 L33 30 Q32 34 28 34 Q12 32 10 16 Q10 12 15 11 Z" fill="var(--green)"/>
      </svg>
      <span class="phone-number">865 471 3908</span>
    </div>

    <p class="website">WWW.BRIGHTFERNPS-EXAMPLE.COM</p>
  </main>
</body>
</html>
```